Website for the K7LAVE-Nest research laboratory.

We are a research team working on personality disorders. We would like a website that presents the team members (noting that students change frequently), ongoing projects with active recruitments, the latest publications, student resources, and possibly patient resources.

We have already prepared the logo with Makerflock.

Our research areas:
1- Lifestyle Medicine and BPD
This area focuses on understanding lifestyle habits and their impact on the health of individuals living with Borderline Personality Disorder (BPD). It aims to improve essential components such as sleep, physical activity, and nutrition by identifying and promoting favorable lifestyle habits. The goal is to strengthen emotional regulation and improve overall health by fully integrating the physical dimension into recovery.
2- Interventions Supporting Psychosocial Functioning
Develop the full recovery potential and enhance social and professional integration strategies to support the life journey of patients in all its dimensions. This area focuses on practices and interventions that facilitate a return to an active life and harmonious integration into society.
3- Optimization of Psychotherapeutic Strategies in BPD
Optimize psychotherapeutic approaches for BPD by identifying the most effective methods, adapting them to individual needs, and evaluating their long-term impact. This research area aims to refine and personalize treatments to maximize their therapeutic benefits.
4- Biological Treatments for BPD: Neuromodulation and Pharmacotherapy
Develop and evaluate biological treatments, particularly in neuromodulation and pharmacotherapy, to improve the management of BPD. This area aims to explore scientific advances in these fields to offer complementary and innovative therapeutic options.

Vision
Affiliated with TOBLAVE, our laboratory is dedicated to creating tomorrow's interventions to offer a hopeful future for individuals living with Borderline Personality Disorder. We design and develop innovative solutions that integrate and value each individual, their loved ones, and their community, supporting their personal, social, functional, and physical recovery.

Values

Innovation
Our commitment to innovation guides every step of our research and development. We continually strive to push the boundaries of knowledge and techniques to create new and bold therapeutic solutions tailored to the evolving needs of individuals living with Borderline Personality Disorder.
Hope
We carry the hope of making a real difference in the lives of people living with BPD. This hope drives our work, pushing us to explore therapeutic approaches that offer patients a better and more serene future. By integrating this hope into our research, we are committed to developing interventions that inspire and support the recovery process. Through our research work, we wish to instill and spread hope.
Empathy and Personalization
We believe in a person-centered and inclusive approach where each individual is considered in their uniqueness and with compassion. By actively integrating patients and their experiences into our research, we aim to design solutions that not only meet their specific needs but also value their recovery while respecting their values. We wish to improve the satisfaction of individuals within the care network, promote the integration of their loved ones and their community.

```html
<!DOCTYPE html>
<html lang="en">
<head>
<meta charset="utf-8">
<title>K7LAVE-Nest — Research Laboratory</title>
<link rel="stylesheet" href="https://fonts.googleapis.com/css2?family=Figtree:wght@400;500;600;700;800&family=Jost:wght@400;500&display=swap">
<style>
:root{
  --blue:#0a86c9;
  --blue-deep:#0670b0;
  --green:#3db53d;
  --green-soft:#d9f0dc;
  --orange:#ef7d1a;
  --ink:#1d2430;
  --muted:#4d5563;
  --pale:#eef6fa;
  --white:#ffffff;
}
*{box-sizing:border-box;margin:0;padding:0}
html,body{width:1200px;height:3117px;overflow:hidden}
body{position:relative;font-family:"Jost",sans-serif;color:var(--ink);background:var(--white)}
.abs{position:absolute}
h1,h2,h3,.heading{font-family:"Figtree",sans-serif;font-weight:700;letter-spacing:-0.5px}
.btn{display:inline-flex;align-items:center;justify-content:center;border-radius:40px;font-family:"Figtree",sans-serif;font-weight:700;font-size:12px;text-decoration:none;color:var(--white);background:var(--green)}
.btn-outline{background:var(--white);color:var(--green);border:1.5px solid var(--green)}
.rule{width:40px;height:3px;background:var(--orange)}

/* top notice */
.notice{top:0;left:0;width:1200px;height:27px;background:var(--blue);color:var(--white);font-family:"Figtree",sans-serif;font-size:10px;font-weight:600;display:flex;align-items:center;justify-content:center}
.notice a{color:var(--white);margin-left:4px}

/* header */
.site-header{top:27px;left:0;width:1200px;height:58px;background:var(--white);display:flex;align-items:center;padding:0 121px}
.brand{display:flex;align-items:center;gap:8px;font-family:"Figtree",sans-serif;font-weight:700;font-size:26px;color:var(--blue)}
.brand-dot{width:32px;height:32px;border-radius:50%;background:var(--green)}
.nav{display:flex;gap:20px;margin-left:auto;font-family:"Figtree",sans-serif;font-weight:600;font-size:11px;color:var(--ink);align-items:center}
.nav .search{width:16px;height:16px;margin-left:2px}
.header-actions{display:flex;gap:8px;margin-left:22px}
.header-actions .btn{height:30px;padding:0 17px}
.header-actions .btn-blue{background:var(--blue)}

/* hero */
.hero{top:85px;left:0;width:1200px;height:620px;overflow:hidden}
.hero-photo{position:absolute;inset:0;background:linear-gradient(100deg,#36506a 0%,#46637c 30%,#8db0c8 55%,#d9e6ef 75%,#b9cfe0 100%)}
.hero-shade{position:absolute;inset:0;background:linear-gradient(90deg,rgba(25,40,58,.75) 0%,rgba(25,40,58,.45) 40%,rgba(25,40,58,0) 62%)}
.hero-eyebrow{top:200px;left:121px;color:var(--white);font-family:"Figtree",sans-serif;font-weight:700;font-size:11px;letter-spacing:1.8px}
.hero-title{top:210px;left:121px;width:540px;color:var(--white);font-size:53px;line-height:53px;letter-spacing:-1.5px}
.hero-text{top:380px;left:121px;width:450px;color:var(--white);font-size:13.5px;line-height:20px}
.hero-btn{top:439px;left:121px;width:192px;height:37px}
.hero-wave{top:520px;left:0;width:1200px;height:190px}

/* vision */
.vision-photo{top:594px;left:121px;width:470px;height:470px;border-radius:50%;background:radial-gradient(circle at 45% 40%,#c9d6df,#7a93a8 70%,#5f7b93)}
.vision-inset{top:826px;left:463px;width:196px;height:196px;border-radius:50%;border:5px solid var(--white);background:linear-gradient(160deg,#9fc7e3,#5a8fb6 60%,#c9b59b)}
.vision-title{top:754px;left:691px;font-size:46px;color:var(--blue)}
.vision-rule{top:809px;left:691px}
.vision-text{top:831px;left:691px;width:400px;font-size:12px;line-height:19px;color:var(--muted)}
.vision-btn{top:966px;left:691px;width:192px;height:37px}

/* research */
.research{top:1113px;left:0;width:1200px;height:527px;background:var(--pale)}
.section-title{left:0;width:1200px;text-align:center;font-size:47px;color:var(--blue)}
.research-title{top:1152px}
.research-rule{top:1211px;left:580px}
.research-intro{top:1229px;left:240px;width:720px;text-align:center;font-size:12px;line-height:19px;color:var(--muted)}
.area{top:1292px;width:230px}
.area-icon{width:100px;height:100px;border-radius:50%;border:7px solid var(--green-soft);background:var(--white);display:flex;align-items:center;justify-content:center}
.area-icon svg{width:42px;height:42px;stroke:var(--green);fill:none;stroke-width:2;stroke-linecap:round;stroke-linejoin:round}
.area h3{margin-top:14px;font-size:18.5px;line-height:20px;color:var(--blue);letter-spacing:-0.3px;min-height:60px}
.area p{margin-top:8px;font-size:10.5px;line-height:17.5px;color:var(--muted)}
.area a{display:block;margin-top:8px;font-family:"Figtree",sans-serif;font-weight:700;font-size:11px;color:var(--green)}

/* values */
.values-band{top:1640px;left:0;width:1200px;height:460px;background:linear-gradient(90deg,#0c7cc0,#0a8ad0 50%,#0b7cc2)}
.values-wave{top:1960px;left:0;width:1200px;height:160px}
.values-fade{top:2100px;left:0;width:1200px;height:420px;background:linear-gradient(180deg,#f1f7fb,#ffffff)}
.values-title{top:1682px;color:var(--white);font-size:47px}
.values-rule{top:1738px;left:580px}
.value-card{top:1773px;width:306px;height:526px;background:var(--white);border-radius:153px 153px 120px 120px;box-shadow:0 10px 30px rgba(10,60,100,.12);text-align:center}
.value-photo{position:absolute;top:12px;left:10px;width:286px;height:286px;border-radius:50%}
.value-card h3{position:absolute;left:0;width:100%;color:var(--blue);font-size:32px;line-height:32px}
.value-card p{position:absolute;left:40px;width:226px;font-size:12px;line-height:19px;color:var(--muted)}
.value-card .btn{position:absolute;left:99px;width:116px;height:35px;font-size:11px}

/* therapy */
.therapy-title{top:2340px;font-size:47px;line-height:47px}
.therapy-rule{top:2443px;left:580px}
.therapy-text{top:2462px;left:250px;width:700px;text-align:center;font-size:12px;line-height:19px;color:var(--muted)}
.therapy-btn{top:2516px;left:504px;width:192px;height:37px}
.therapy-photo{top:2560px;left:0;width:1200px;height:326px;background:linear-gradient(180deg,#ffffff 0%,#f3e6cf 18%,#e7b873 45%,#c98a3e 70%,#8a5a2a 100%)}

/* footer */
.site-footer{top:2886px;left:0;width:1200px;height:231px;background:#f1f7fb}
.footer-brand{top:2920px;left:121px}
.footer-brand .brand{font-size:29px}
.footer-copy{top:2964px;left:121px;font-size:10.5px;color:var(--muted)}
.social{top:2994px;left:121px;display:flex;gap:7px}
.social span{width:31px;height:31px;border-radius:50%;background:var(--green)}
.footer-col{top:2921px}
.footer-col h4{font-family:"Figtree",sans-serif;font-weight:600;font-size:14px;color:var(--blue);margin-bottom:8px}
.footer-col li{list-style:none;font-size:10.5px;line-height:21.5px;color:var(--muted)}
.footer-col a{color:var(--green);font-weight:500}
</style>
</head>
<body>

<div class="abs notice">In some cases, you may not know that you have a personality disorder. Get our expert guidance. <a href="#">Learn More</a></div>

<header class="abs site-header">
  <div class="brand"><span class="brand-dot"></span>K7LAVE-Nest</div>
  <nav class="nav">
    <span>Mental Health Information</span><span>Research</span><span>Funding</span><span>Resources</span><span>About Us</span>
    <svg class="search" viewBox="0 0 16 16" fill="none" stroke="#ef7d1a" stroke-width="2"><circle cx="7" cy="7" r="5"/><path d="M11 11l4 4"/></svg>
  </nav>
  <div class="header-actions">
    <a class="btn btn-blue" href="#">Get Involved</a>
    <a class="btn" href="#">Contact Us</a>
  </div>
</header>

<section class="abs hero">
  <div class="hero-photo" role="img" aria-label="Researcher in safety glasses looking into a laboratory microscope"></div>
  <div class="hero-shade"></div>
</section>
<div class="abs hero-eyebrow">EXTENSIVE RESEARCH AND DEVELOPMENT</div>
<h1 class="abs hero-title">Providing Psychiatric and Behavioral Health Care Information.</h1>
<p class="abs hero-text">Our team uses the most up-to-date, evidence-based treatments that emphasize patients' growth on their journey.</p>
<a class="abs btn hero-btn" href="#">Discover More Information</a>
<svg class="abs hero-wave" viewBox="0 0 1200 190" preserveAspectRatio="none"><path d="M0 152 C140 70 290 28 430 25 C600 22 690 112 880 110 C1030 108 1140 70 1200 45 L1200 190 L0 190 Z" fill="#ffffff"/></svg>

<section>
  <div class="abs vision-photo" role="img" aria-label="Clinical team of doctors and nurses talking in a hospital hallway"></div>
  <div class="abs vision-inset" role="img" aria-label="Older couple laughing together outdoors"></div>
  <h2 class="abs vision-title">Our Vision</h2>
  <div class="abs rule vision-rule"></div>
  <p class="abs vision-text">Affiliated with TOBLAVE, our laboratory is dedicated to creating tomorrow's interventions to offer a hopeful future for individuals living with Borderline Personality Disorder. We design and develop innovative solutions that integrate and value each individual, their loved ones, and their community, supporting their personal, social, functional, and physical recovery.</p>
  <a class="abs btn vision-btn" href="#">Discover More Information</a>
</section>

<section>
  <div class="abs research"></div>
  <h2 class="abs section-title research-title">Our Research Areas</h2>
  <div class="abs rule research-rule"></div>
  <p class="abs research-intro">Borderline personality disorder is a serious mental disorder marked by a pattern of instability in moods, behavior, self-image, and functioning. Additional information about borderline personality disorder can be found here.</p>

  <article class="abs area" style="left:121px">
    <div class="area-icon"><svg viewBox="0 0 24 24"><rect x="5" y="3" width="11" height="3" rx="1"/><path d="M6 6v14h8"/><path d="M9 10h4M9 13h4M9 16h2"/><rect x="14" y="15" width="7" height="4" rx="2"/></svg></div>
    <h3>Lifestyle Medicine and Borderline Personality Disorder</h3>
    <p>This area focuses on understanding lifestyle habits and their impact on the health of individuals living with Borderline Personality Disorder (BPD). It aims to improve essential components.</p>
    <a href="#">Learn More</a>
  </article>
  <article class="abs area" style="left:364px">
    <div class="area-icon"><svg viewBox="0 0 24 24"><circle cx="12" cy="5" r="2"/><circle cx="5" cy="12" r="2"/><circle cx="19" cy="12" r="2"/><path d="M9 11a3 3 0 0 1 6 0"/><path d="M2 20a3 3 0 0 1 6 0M16 20a3 3 0 0 1 6 0"/><path d="M10 20h4"/></svg></div>
    <h3 style="margin-top:22px;min-height:52px">Interventions Supporting Psychosocial Functioning</h3>
    <p>Develop the full recovery potential and enhance social and professional integration strategies to support the life journey of patients in all its dimensions. This area focuses on practices and interventions.</p>
    <a href="#">Learn More</a>
  </article>
  <article class="abs area" style="left:609px">
    <div class="area-icon"><svg viewBox="0 0 24 24"><rect x="4" y="4" width="16" height="16" rx="2"/><path d="M4 8h16"/><circle cx="12" cy="14" r="2.5"/><path d="M12 10v1.2M12 16.8V18M8 14h1.2M14.8 14H16"/></svg></div>
    <h3>Optimization of Psychotherapeutic Strategies in BPD</h3>
    <p>Optimize psychotherapeutic approaches for BPD by identifying the most effective methods, adapting them to individual needs, and evaluating their long-term impact. This research area aims to refine.</p>
    <a href="#">Learn More</a>
  </article>
  <article class="abs area" style="left:853px">
    <div class="area-icon"><svg viewBox="0 0 24 24"><path d="M6 3h8l5 5v13H6z"/><path d="M14 3v5h5"/><path d="M12.5 12v6M9.5 15h6"/></svg></div>
    <h3>Biological Treatments for BPD: Neuromodulation and Pharmacotherapy</h3>
    <p>Develop and evaluate biological treatments, particularly in neuromodulation and pharmacotherapy, to improve the management of BPD. This area aims to explore scientific advances in these fields.</p>
    <a href="#">Learn More</a>
  </article>
</section>

<section>
  <div class="abs values-band"></div>
  <div class="abs values-fade"></div>
  <svg class="abs values-wave" viewBox="0 0 1200 160" preserveAspectRatio="none"><path d="M0 120 C180 40 380 20 600 50 C820 80 1020 40 1200 0 L1200 160 L0 160 Z" fill="#f1f7fb"/></svg>
  <h2 class="abs section-title values-title">We Stick To Our Own Values</h2>
  <div class="abs rule values-rule"></div>

  <article class="abs value-card" style="left:121px">
    <div class="value-photo" role="img" aria-label="Two lab researchers in white coats reviewing a tablet" style="background:linear-gradient(150deg,#d9dde2,#9aa6b2 60%,#6f7b88)"></div>
    <h3 style="top:342px">Innovation</h3>
    <p style="top:382px">Our commitment to innovation guides every step of our research and development. We continually strive to push the boundaries of knowledge.</p>
    <a class="btn btn-outline" href="#" style="top:458px">Learn More</a>
  </article>
  <article class="abs value-card" style="left:447px">
    <div class="value-photo" role="img" aria-label="Doctor comforting an older patient by holding her hands" style="background:linear-gradient(150deg,#e6e9ec,#c9b9a8 55%,#8aa0b3)"></div>
    <h3 style="top:323px">Empathy and Personalization</h3>
    <p style="top:400px">We believe in a person-centered and inclusive approach where each individual is considered.</p>
    <a class="btn btn-outline" href="#" style="top:458px">Learn More</a>
  </article>
  <article class="abs value-card" style="left:773px">
    <div class="value-photo" role="img" aria-label="Close-up of two hands resting on each other" style="background:radial-gradient(circle at 50% 55%,#c98f73,#8a5a46 60%,#5a3a30)"></div>
    <h3 style="top:340px">Hope</h3>
    <p style="top:382px">We carry the hope of making a real difference in the lives of people living with BPD. This hope drives our work, pushing us to explore.</p>
    <a class="btn btn-outline" href="#" style="top:458px">Learn More</a>
  </article>
</section>

<section>
  <h2 class="abs section-title therapy-title">Therapy Focuses On Treating<br>Dangerous Behavior</h2>
  <div class="abs rule therapy-rule"></div>
  <p class="abs therapy-text">Personality disorders can seriously disrupt your life and the lives of those who care about you. They may cause issues in relationships, work or school. Our team approach is needed to meet your mental, medical and social needs.</p>
  <a class="abs btn therapy-btn" href="#">Discover More Information</a>
  <div class="abs therapy-photo" role="img" aria-label="Family running with outstretched arms through a golden field at sunset"></div>
</section>

<footer>
  <div class="abs site-footer"></div>
  <div class="abs footer-brand"><div class="brand"><span class="brand-dot"></span>K7LAVE-Nest</div></div>
  <div class="abs footer-copy">© 2025 K7LAVE-Nest. All rights reserved.</div>
  <div class="abs social" aria-label="Social links"><span></span><span></span><span></span><span></span></div>

  <div class="abs footer-col" style="left:347px"><h4>About K7LAVE-Nest</h4><ul><li>Our Story</li><li>Locations</li><li>Health Information Policy</li><li>Media Requests</li><li>Price Transparency</li><li>Contact Us</li></ul></div>
  <div class="abs footer-col" style="left:509px"><h4>Resources</h4><ul><li>Health Topics</li><li>Brochures and Fact Sheets</li><li>Información en español</li><li>Health and Human Services</li><li>Media Requests</li><li>News Network</li></ul></div>
  <div class="abs footer-col" style="left:680px"><h4>Contact Us</h4><ul><li>Phone:&nbsp; 1-555-204-3318</li><li>Live Online Chat:&nbsp; <a href="#">Talk to a Representative</a></li><li>Email:&nbsp; hello@k7lavenest.org</li><li style="margin-top:10px;line-height:17px">Head Office: 24 Alder Grove Lane, Brookvale,<br>BV 40218, Northland</li></ul></div>
  <div class="abs footer-col" style="left:937px"><h4>Policies and Notices</h4><ul><li>Privacy Policy</li><li>Website Policies</li><li>FOIA</li><li>Accessibility</li><li>Agency Vulnerability Disclosure</li><li>Disclaimer</li></ul></div>
</footer>

</body>
</html>
```